Re-design existing website and add products for sale.

Our current website is very basic and cluttered. (brightwillowcare.com.au)We want a modern looking website that is easy to navigate. We also want to start selling essential oils and crystal products, so there needs to be a separate page for this. Also needs to be easily edited as we need to change the monthly oracle card with the description. Would like calming colours as we are all about natural healing. Alongside the services listed there should be a button to book now which asks for their name, email, phone number ect. and adds it to the cart.

• Logo is still being designed, please leave a space for the logo which will basically be a lotus flower within a mandala.

```html
<!DOCTYPE html>
<html lang="en">
<head>
<meta charset="utf-8">
<title>Bright Willow Care</title>
<link rel="stylesheet" href="https://fonts.googleapis.com/css2?family=Lato:wght@400;700&display=swap">
<style>
:root{
  --purple:#7a3ea6;
  --pink:#e47cb8;
  --pink-soft:#f6c9e3;
  --lavender:#dcc3ec;
  --lavender-btn:#c9a4de;
  --footer-bg:#e3c7ef;
  --text:#333;
  --muted:#777;
  --line:#e3e3e3;
  --white:#fff;
}
*{box-sizing:border-box;margin:0;padding:0}
html,body{width:1200px;height:2848px;overflow:hidden;background:var(--white);font-family:"Lato",Arial,sans-serif;color:var(--text)}
.page{position:relative;width:1200px;height:2848px}
.abs{position:absolute}
.brand{left:100px;top:18px}
.brand-name{font-size:40px;font-weight:700;color:var(--purple);display:flex;align-items:center;gap:12px}
.brand-mark{width:18px;height:18px;border-radius:50%;background:var(--pink)}
.brand-tag{font-size:13px;color:var(--muted);margin-top:6px;font-style:normal}
.social{left:795px;top:44px;display:flex;gap:32px}
.social span{width:14px;height:14px;border-radius:50%;background:var(--purple);display:block}
.call{left:1040px;top:0;width:160px;height:112px;background:var(--pink-soft);text-align:center;padding-top:30px;font-size:22px;color:#222;line-height:1.2}
.nav{left:0;top:112px;width:1200px;height:44px;border-top:1px solid var(--line);border-bottom:1px solid var(--line)}
.nav ul{list-style:none;display:flex;gap:24px;position:absolute;left:118px;top:13px;font-size:14px;color:var(--purple);letter-spacing:.5px}
.cart{left:1052px;top:122px}
.hero{left:0;top:166px;width:1200px;height:524px;background:linear-gradient(100deg,#5a4a24 0%,#b7893e 30%,#8e5a3a 55%,#c07a3e 75%,#5c5a2a 100%)}
.hero-box{left:112px;top:268px;width:328px;height:276px;background:var(--white);padding:30px 26px}
.hero-box h1{font-size:36px;line-height:1.25;font-weight:700;color:#222}
.hero-box p{font-size:17px;color:#555;margin:14px 0 22px}
.btn{display:inline-block;background:var(--lavender-btn);color:var(--white);font-size:13px;padding:8px 18px;border-radius:2px}
.card{overflow:hidden}
.card .ph{position:absolute;inset:0}
.card .cap{position:absolute;left:32px;bottom:34px;color:var(--white)}
.card .cap h3{font-size:30px;font-weight:400;color:#fff;text-shadow:0 1px 2px rgba(0,0,0,.25)}
.card .cap p{font-size:13px;margin:6px 0 14px;color:#f4eef8}
.intro-card{background:linear-gradient(135deg,#e9d3f2,#cfa8e4);padding:60px 40px}
.intro-card h2{font-size:30px;font-weight:400;color:#333;line-height:1.2}
.intro-card p{font-size:13px;color:#555;margin:16px 0 20px;line-height:1.5}
.intro-card .btn{background:var(--white);color:var(--purple)}
.section-title{left:0;top:1892px;width:1200px;text-align:center;font-size:36px;font-weight:400;color:#333}
.product{width:184px}
.product .box{height:212px;border:1px solid var(--line);position:relative;display:flex;align-items:center;justify-content:center}
.product .name{text-align:center;color:var(--purple);font-size:20px;margin-top:22px}
.product .price{text-align:center;font-size:17px;margin-top:6px}
.view-all{left:518px;top:2332px;width:164px;height:44px;background:var(--pink-soft);color:var(--purple);font-size:16px;text-align:center;line-height:44px}
.footer{left:100px;top:2420px;width:1016px;height:340px;background:var(--footer-bg);padding:50px 62px}
.fcol{position:absolute;top:54px}
.fcol h4{font-size:24px;font-weight:400;color:#333;margin-bottom:18px}
.fcol li{list-style:none;font-size:13px;color:#444;line-height:2}
.sub-input{width:240px;height:38px;background:var(--white);font-size:13px;color:#888;padding:11px 12px}
.sub-btn{width:240px;height:38px;background:var(--pink);color:#fff;font-size:14px;text-align:center;line-height:38px;margin-top:12px}
.copy{left:0;top:2806px;width:1200px;text-align:center;font-size:13px;color:var(--muted)}
</style>
</head>
<body>
<div class="page">

  <header>
    <div class="abs brand">
      <div class="brand-name"><span class="brand-mark"></span>Bright Willow Care</div>
      <div class="brand-tag">Heal Your Soul, Find Inner Peace &amp; Balance in Your Life</div>
    </div>
    <div class="abs social" aria-label="Social links"><span></span><span></span><span></span></div>
    <div class="abs call">Call Us<br>123-555-0147</div>
  </header>

  <nav class="abs nav">
    <ul>
      <li>ABOUT US</li><li>OUR SERVICES</li><li>PRODUCTS</li><li>WHY US</li><li>BLOGS</li><li>TESTIMONIAL</li><li>CONTACT</li>
    </ul>
  </nav>
  <svg class="abs cart" width="30" height="24" viewBox="0 0 30 24" aria-label="Cart">
    <path d="M1 3h4l3 12h12l3-9H7" fill="none" stroke="#7a3ea6" stroke-width="2"/>
    <circle cx="10" cy="20" r="2" fill="#7a3ea6"/><circle cx="19" cy="20" r="2" fill="#7a3ea6"/>
    <circle cx="25" cy="6" r="5" fill="#e47cb8"/>
  </svg>

  <section class="abs hero" role="img" aria-label="Photo of a woman meditating with hands in prayer among autumn leaves"></section>
  <div class="abs hero-box">
    <h1>Spiritual Healing Sessions to Relax Mind &amp; body</h1>
    <p>Pellentesque faucibus accums</p>
    <span class="btn">Book Now</span>
  </div>

  <section class="services">
    <div class="abs card intro-card" style="left:100px;top:740px;width:240px;height:320px">
      <h2>Bright<br>Willow Care</h2>
      <p>Nam quis fringilla velit, ut iaculis erat nec healing comfort.</p>
      <span class="btn">Book Now</span>
    </div>
    <div class="abs card" style="left:360px;top:740px;width:408px;height:320px">
      <div class="ph" role="img" aria-label="Photo of a hand held over a person during Reiki healing" style="background:linear-gradient(135deg,#f2ecef,#d9cfd6)"></div>
      <div class="cap"><h3>Reiki &amp; Seichim Healings</h3><p>Pellentesque faucibus accumsan</p><span class="btn">Book Now</span></div>
    </div>
    <div class="abs card" style="left:788px;top:740px;width:328px;height:320px">
      <div class="ph" role="img" aria-label="Illustration of a glowing figure with chakra energy points" style="background:linear-gradient(160deg,#e9a8e6,#9fc8f0)"></div>
      <div class="cap"><h3>Energy Healing</h3><p>Pellentesque faucibus accumsan</p><span class="btn">Book Now</span></div>
    </div>

    <div class="abs card" style="left:100px;top:1128px;width:324px;height:320px">
      <div class="ph" role="img" aria-label="Photo of hands placing a crystal during chakra balancing" style="background:linear-gradient(150deg,#a9c58a,#e8d9c9)"></div>
      <div class="cap"><h3>Chakra Balancing</h3><p>Pellentesque faucibus accumsan</p><span class="btn">Book Now</span></div>
    </div>
    <div class="abs card" style="left:448px;top:1128px;width:668px;height:320px">
      <div class="ph" role="img" aria-label="Photo of hands giving an energy balancing treatment" style="background:linear-gradient(120deg,#c9b3a8,#e9dcd5 60%,#cdbfb8)"></div>
      <div class="cap"><h3>Energy Balancing</h3><p>Pellentesque faucibus accumsan</p><span class="btn">Book Now</span></div>
    </div>

    <div class="abs card" style="left:100px;top:1512px;width:660px;height:320px">
      <div class="ph" role="img" aria-label="Photo of a person resting while a healer holds hands above them" style="background:linear-gradient(120deg,#d8d2d4,#c6a89a 55%,#ece6e6)"></div>
      <div class="cap"><h3>Past Life Clearing</h3><p>Pellentesque faucibus accumsan</p><span class="btn">Book Now</span></div>
    </div>
    <div class="abs card" style="left:784px;top:1512px;width:332px;height:320px">
      <div class="ph" role="img" aria-label="Illustration of open hands surrounded by soft violet light" style="background:linear-gradient(160deg,#c9a0e0,#f0d5f2 50%,#b48ad6)"></div>
      <div class="cap"><h3>Distant Healing</h3><p>Pellentesque faucibus accumsan</p><span class="btn">Book Now</span></div>
    </div>
  </section>

  <h2 class="abs section-title">Our Products</h2>
  <section class="products">
    <div class="abs product" style="left:100px;top:1968px"><div class="box"><div role="img" aria-label="Amber essential oil bottle" style="width:50px;height:110px;background:linear-gradient(#6b3a1a,#b5651d);border-radius:6px"></div></div><div class="name">Product Name</div><div class="price">$25.00</div></div>
    <div class="abs product" style="left:304px;top:1968px"><div class="box"><div role="img" aria-label="Dark essential oil bottle with white label" style="width:44px;height:120px;background:linear-gradient(#222,#555);border-radius:5px"></div></div><div class="name">Product Name</div><div class="price">$25.00</div></div>
    <div class="abs product" style="left:508px;top:1968px"><div class="box"><div role="img" aria-label="Round silver balm tin" style="width:110px;height:110px;background:radial-gradient(#f2f2f2,#a9a9a9);border-radius:50%"></div></div><div class="name">Product Name</div><div class="price">$25.00</div></div>
    <div class="abs product" style="left:712px;top:1968px"><div class="box"><div role="img" aria-label="Amber dropper bottle" style="width:46px;height:140px;background:linear-gradient(#3a2a20,#b0561d);border-radius:6px"></div></div><div class="name">Product Name</div><div class="price">$25.00</div></div>
    <div class="abs product" style="left:916px;top:1968px"><div class="box"><div role="img" aria-label="Small amber oil vial" style="width:40px;height:96px;background:linear-gradient(#c46a1a,#e09040);border-radius:5px"></div></div><div class="name">Product Name</div><div class="price">$25.00</div></div>
  </section>
  <div class="abs view-all">View All</div>

  <footer class="abs footer">
    <div class="fcol" style="left:62px"><h4>Contact us</h4><ul><li>100 Maple Grove Lane</li><li>Springfield, VIC 3000</li><li>Tel: 123-555-0147</li><li>View Our Map</li></ul></div>
    <div class="fcol" style="left:310px"><h4>Quick links</h4><ul><li>Home</li><li>About Us</li><li>Services</li><li>Contact Us</li></ul></div>
    <div class="fcol" style="left:524px"><h4>Resources</h4><ul><li>Our Products</li><li>Why Us</li><li>Shop Now</li><li>Our Blogs</li></ul></div>
    <div class="fcol" style="left:700px"><h4>Get Special Deals</h4><div class="sub-input">Email address</div><div class="sub-btn">Subscribe</div></div>
  </footer>
  <p class="abs copy">© 2019 Company Name. All right reserved.</p>
</div>
</body>
</html>
```